website design for a new age Real Estate Security Business

We are launching a business in real estate which no body else is doing. We are going to use technology in terms of software and hardware to provide our services.

We are going to use Big Data, IOT etc.. for our services.

NOTE: We don't want to see Shiel or buildings etc.. that directly suggests Real estate or security on this design

Target Market(s)

India

Industry/Entity Type

Real Estate

Number of Pages Required

4 page

Font styles to use
Sans Serif
Other font styles liked:
• Use Google Fonts

Requirements
Must have
• Home Page should be trendy and colourful should give user confidence to subscribe to our service.
Nice to have
• Use Google fonts.
Should not have
• Design shouldnt have Shield or Buildings that directly suggests real estate or security.

```html
<!DOCTYPE html>
<html lang="en">
<head>
<meta charset="utf-8">
<title>VaultNest – Doc Secure</title>
<link rel="stylesheet" href="https://fonts.googleapis.com/css2?family=Montserrat:wght@400;500;600&family=Open+Sans:wght@400;600;700&family=Oswald:wght@400&family=Arimo&display=swap">
<style>
:root{
  --navy:#1a4a6b;
  --ink:#111;
  --grey-text:#8b8b8b;
  --soft-grey:#9a9a9a;
  --footer-bg:#8f979c;
  --rule:#d6d6d6;
  --white:#fff;
}
*{margin:0;padding:0;box-sizing:border-box}
html,body{width:762px;height:1200px;overflow:hidden;background:var(--white)}
body{position:relative;font-family:"Arimo",Arial,sans-serif;color:var(--ink)}
.abs{position:absolute}

/* header */
.site-header{left:0;top:0;width:762px;height:66px;background:linear-gradient(90deg,#f1f2f3,#e6e8ea)}
.brand{left:53px;top:12px;font-family:"Montserrat",sans-serif;font-weight:400;font-size:33px;color:var(--navy);letter-spacing:-.5px}
.nav{top:16px;left:344px;height:26px;display:flex;align-items:center;font-family:"Open Sans",sans-serif;font-size:10px;color:#555}
.nav a{text-decoration:none;color:inherit;position:absolute;white-space:nowrap;top:7px}
.nav .active{left:0;top:0;width:60px;height:26px;border-radius:13px;background:#000;color:var(--white);display:flex;align-items:center;justify-content:center}

/* hero */
.page-title{left:0;top:98px;width:762px;text-align:center;font-family:"Montserrat",sans-serif;font-weight:600;font-size:33px;letter-spacing:.5px}
.page-title span{color:var(--navy)}
.hero-visual{left:113px;top:170px;width:196px;height:196px;border-radius:50%;background:radial-gradient(circle at 45% 40%,#ffffff,#e5e7e8 70%,#b9bcbe);box-shadow:2px 3px 0 #a9abad}
.hero-copy{left:369px;top:160px;width:300px}
.hero-copy h2{font-family:"Montserrat",sans-serif;font-weight:500;font-size:21px;color:var(--navy)}
.hero-copy p.lead{margin-top:10px;font-size:8.8px;line-height:14.4px;color:var(--grey-text)}
.price{margin-top:8px;font-family:"Montserrat",sans-serif;font-size:27px;color:var(--ink)}
.price small{font-size:15px;color:#aaa}
.price .cur{font-size:17px;color:#999}
.after{margin-top:2px;font-size:8.8px;color:var(--grey-text)}
.after b{font-family:"Montserrat",sans-serif;font-size:18px;color:var(--navy)}
.order-btn{left:367px;top:314px;width:126px;height:33px;border:1px solid #222;font-family:"Open Sans",sans-serif;font-size:13px;display:flex;align-items:center;justify-content:center}

.divider{left:49px;top:404px;width:664px;height:1px;background:var(--rule)}

/* features */
.section-title{left:0;top:432px;width:762px;text-align:center;font-family:"Montserrat",sans-serif;font-weight:500;font-size:19px;color:var(--soft-grey)}
.section-intro{left:130px;top:461px;width:502px;text-align:center;font-size:8.8px;line-height:14.4px;color:var(--grey-text)}
.feature{top:508px;width:210px;text-align:center}
.feature .icon{width:86px;height:86px;margin:0 auto;border:1px solid #ccc;border-radius:50%;display:flex;align-items:center;justify-content:center}
.feature h3{margin-top:10px;font-family:"Montserrat",sans-serif;font-weight:500;font-size:17px;color:#222}
.feature p{margin-top:8px;font-size:8.8px;line-height:14.4px;color:var(--grey-text)}

/* price pill */
.price-pill{left:216px;top:734px;width:300px;height:72px;border-radius:36px 0 0 36px;background:linear-gradient(90deg,#e6e8e9,#f6f7f7)}
.price-pill .amt{position:absolute;left:24px;top:6px;font-family:"Montserrat",sans-serif;font-size:26px}
.price-pill .amt small{font-size:15px;color:#666}
.price-pill .amt .cur{font-size:16px;color:#888}
.price-pill p{position:absolute;left:23px;top:40px;width:200px;font-size:8.8px;line-height:14.4px;color:#555}
.price-badge{left:444px;top:718px;width:100px;height:100px;border-radius:50%;background:radial-gradient(circle at 45% 35%,#fff,#e3e5e6 75%);box-shadow:1px 2px 0 #b8bbbd;text-align:center}
.price-badge .big{margin-top:28px;font-family:"Montserrat",sans-serif;font-weight:500;font-size:25px;color:var(--ink)}
.price-badge .per{font-family:"Open Sans",sans-serif;font-size:11px;color:var(--navy)}
.badge-shadow{left:444px;top:820px;width:92px;height:6px;border-radius:50%;background:radial-gradient(ellipse,#9a9a9a,transparent 70%)}

/* guarantee */
.guarantee{left:49px;top:868px;width:664px;height:92px;background:var(--navy)}
.seal{left:71px;top:860px;width:110px;height:110px;border-radius:50%;background:var(--white);border:4px solid #222;box-shadow:inset 0 0 0 6px #fff,inset 0 0 0 8px #222}
.guarantee h2{position:absolute;left:151px;top:12px;font-family:"Oswald",sans-serif;font-weight:400;font-size:26px;color:var(--white);letter-spacing:-.3px}
.guarantee p{position:absolute;left:151px;top:52px;width:490px;font-family:"Open Sans",sans-serif;font-size:10.4px;line-height:16px;color:var(--white)}

/* footer */
.site-footer{left:0;top:1002px;width:762px;height:198px;background:var(--footer-bg);font-family:"Open Sans",sans-serif;color:var(--white)}
.foot-brand{position:absolute;left:50px;top:20px;font-family:"Montserrat",sans-serif;font-size:28px;color:var(--navy);letter-spacing:-.5px}
.foot-about{position:absolute;left:50px;top:64px;width:200px;font-size:10.4px;line-height:16px}
.foot-col h4{font-family:"Montserrat",sans-serif;font-weight:600;font-size:12px;color:var(--navy);letter-spacing:.3px}
.contact{position:absolute;left:281px;top:26px;width:200px}
.contact li{list-style:none;position:relative;padding-left:21px;font-size:10.4px;line-height:16px}
.contact li svg{position:absolute;left:2px;top:2px}
.newsletter{position:absolute;left:510px;top:26px;width:204px}
.newsletter p{margin-top:10px;font-size:10.4px}
.newsletter .field{margin-top:6px;width:204px;height:26px;background:#d3d6d8;color:#777;font-size:10.4px;padding:5px 7px}
.newsletter .btn{margin-top:8px;width:98px;height:29px;background:var(--navy);font-weight:700;font-size:10.4px;letter-spacing:.4px;display:flex;align-items:center;justify-content:center}
.foot-rule{position:absolute;left:49px;top:155px;width:664px;height:1px;background:#555}
.copyright{position:absolute;left:50px;top:164px;font-size:10.4px}
.copyright b{color:var(--navy)}
.social{position:absolute;top:161px;width:30px;height:30px;border-radius:50%;border:1px solid var(--white)}
.social.filled{background:var(--navy);border-color:var(--navy)}
</style>
</head>
<body>

<header class="abs site-header">
  <div class="abs brand">VaultNest</div>
  <nav class="abs nav">
    <a class="active" href="#">HOME</a>
    <a href="#" style="left:81px">ABOUT US</a>
    <a href="#" style="left:165px">SERVICES</a>
    <a href="#" style="left:247px">PRICING</a>
    <a href="#" style="left:323px">CONTACT</a>
  </nav>
</header>

<h1 class="abs page-title"><span>DOC</span> SECURE</h1>

<div class="abs hero-visual" role="img" aria-label="Illustration of a folder with a padlock"></div>

<div class="abs hero-copy">
  <h2>Doc Secure</h2>
  <p class="lead">Lorem Ipsum is simply dummy text of the printing and typesetting industry. Lorem Ipsum has been the industry's standard dummy text ever since the 1500s.</p>
  <div class="price"><span class="cur">₹</span>1000<small>/year</small></div>
  <div class="after">for every document after that <b>₹500</b>/Year.</div>
</div>
<div class="abs order-btn">ORDER NOW</div>

<div class="abs divider"></div>

<h2 class="abs section-title">TO KEEP YOUR PROPERTY SAFE</h2>
<p class="abs section-intro">Lorem Ipsum is simply dummy text of the printing and typesetting industry. Lorem Ipsum has been the industry's standard dummy text ever since the 1500s.</p>

<div class="abs feature" style="left:45px">
  <div class="icon">
    <svg width="34" height="30" viewBox="0 0 34 30" fill="#1a4a6b">
      <circle cx="17" cy="8" r="6"/><circle cx="7" cy="10" r="4.5"/><circle cx="27" cy="10" r="4.5"/>
      <path d="M7 29c0-8 4-13 10-13s10 5 10 13z"/><path d="M0 25c0-6 3-9 7-9 2 0 3 1 4 2-2 2-3 5-3 7z"/><path d="M34 25c0-6-3-9-7-9-2 0-3 1-4 2 2 2 3 5 3 7z"/>
    </svg>
  </div>
  <h3>User Friendly</h3>
  <p>Lorem Ipsum is simply dummy text of the printing and typesetting industry. Lorem Ipsum has been the industry's standard dummy text ever since the 1500s.</p>
</div>

<div class="abs feature" style="left:275px">
  <div class="icon">
    <svg width="24" height="40" viewBox="0 0 24 40"><path d="M20 12c0-3-3-5-8-5s-8 2-8 6 3 5 8 6 8 3 8 7-3 6-8 6-8-2-8-5M12 2v36" fill="none" stroke="#1a4a6b" stroke-width="4" stroke-linecap="round"/></svg>
  </div>
  <h3>Affordable</h3>
  <p>Lorem Ipsum is simply dummy text of the printing and typesetting industry. Lorem Ipsum has been the industry's standard dummy text ever since the 1500s.</p>
</div>

<div class="abs feature" style="left:505px">
  <div class="icon">
    <svg width="40" height="42" viewBox="0 0 40 42" fill="none" stroke="#1a4a6b" stroke-width="3.5" stroke-linejoin="round">
      <rect x="2" y="18" width="8" height="20" fill="#1a4a6b"/>
      <path d="M12 20l8-9c2-3 2-7 4-8 4 0 5 4 4 8l-2 6h9c3 0 4 3 3 5l-3 13c-1 2-2 3-4 3H12z"/>
    </svg>
  </div>
  <h3>Satisfaction</h3>
  <p>Lorem Ipsum is simply dummy text of the printing and typesetting industry. Lorem Ipsum has been the industry's standard dummy text ever since the 1500s.</p>
</div>

<div class="abs price-pill">
  <div class="amt"><span class="cur">₹</span>1000<small>/year</small></div>
  <p>Lorem Ipsum is simply dummy text of the printing and typesetting industry.</p>
</div>
<div class="abs badge-shadow"></div>
<div class="abs price-badge">
  <div class="big">₹500</div>
  <div class="per">PER YEAR</div>
</div>

<section class="abs guarantee">
  <h2>VAULTNEST 100% SATISFACTION GUARANTEED</h2>
  <p>Lorem Ipsum is simply dummy text of the printing and typesetting industry. Lorem Ipsum has been the industry's standard dummy text ever since the 1500.</p>
</section>
<div class="abs seal" role="img" aria-label="Satisfaction guarantee seal"></div>

<footer class="abs site-footer">
  <div class="foot-brand">VaultNest</div>
  <p class="foot-about">Lorem Ipsum is simply dummy text of the printing and typesetting industry. Lorem Ipsum has been the industry's standard dummy text ever since the 1500.</p>

  <div class="foot-col contact">
    <h4>CONTACT INFO</h4>
    <ul style="margin-top:10px">
      <li><svg width="10" height="13" viewBox="0 0 10 13"><path d="M5 0a5 5 0 0 0-5 5c0 3 5 8 5 8s5-5 5-8a5 5 0 0 0-5-5z" fill="#fff"/><circle cx="5" cy="5" r="1.8" fill="#8f979c"/></svg>Lorem Ipsum is simply dummy text of the printing and typesetting industry.</li>
      <li style="margin-top:8px;font-weight:600"><svg width="12" height="12" viewBox="0 0 12 12"><path d="M2 0l2 3-1 1.5c1 2 2.5 3.5 4.5 4.5L9 8l3 2-1 2C5 12 0 7 0 1z" fill="#fff"/></svg>123 456 7890</li>
      <li style="margin-top:8px"><svg width="13" height="10" viewBox="0 0 13 10"><rect x=".6" y=".6" width="11.8" height="8.8" fill="none" stroke="#fff" stroke-width="1.2"/><path d="M.6.6l5.9 5 5.9-5" fill="none" stroke="#fff" stroke-width="1.2"/></svg>info@vaultnest.in</li>
    </ul>
  </div>

  <div class="foot-col newsletter">
    <h4>NEWSLETTER</h4>
    <p>Subscribe to stay in vaultnest.</p>
    <div class="field">Enter email Id</div>
    <div class="btn">SUBSCRIBE</div>
  </div>

  <div class="foot-rule"></div>
  <div class="copyright">© <b>Vaultnest</b> - 2017.All Rights Reserved.</div>
  <div class="social filled" style="left:563px" aria-label="Social link"></div>
  <div class="social" style="left:602px" aria-label="Social link"></div>
  <div class="social" style="left:642px" aria-label="Social link"></div>
  <div class="social" style="left:682px" aria-label="Social link"></div>
</footer>

</body>
</html>
```